Kelvanta (www.kelvanta.net) needs exciting professional PowerPoint pitch template

Kelvanta is an exciting new start-up targeting innovative ways to engage with retail customers at the point of sale.

Our customers are looking for us to help them increase the "wallet share" of their retail customers. The retail customer has their wallet open at the Point of Sale and are paying money to our customer. At Kelvanta we are all about attracting the attention of the retail customer AT THAT POINT IN TIME and engaging the retail customer in spending a little more in that store or another store that has a relationship to the retail customer's purchase.

Our customers are the owners of very large supermarkets, chain stores, and financial institutions, and therefore when we pitch a proposal to these buyers it needs to be slick, professional, and very memorable.

The PowerPoint sales presentation template is a key part of striking that impression.

Here is some background...

Our Vision
Through applying new thinking to a mature industry we are reinventing selected segments of the Australian retail messaging business, generating significant value for our customers, our suppliers, and our owners.
We operate with integrity, agility, and intelligence to doing things smarter, faster and more efficiently.
We bring deep industry expertise, deep relationships with customers and suppliers, and a will to see the old ways give way to smarter ways – this is why we win.
From this economically sustainable platform, we will examine the disruption of other market segments by further leveraging the elements that make us successful.

Our Values
With our clients, with our suppliers, with our staff, and with our owners:
# We Partner – We align the interest of all stakeholders by striving to ensure everything we do is mutually beneficial and commercially sustainable in the long term. We are clear with all our stakeholders about what our expectations are of them, and we seek clarity from them in their expectations of us.
# We Innovate – In the segments we choose to compete in, we bring fresh ideas, new business processes, the right relationships, and the right technology to ensure the supply chain is nimble, competitive, and reliable.
# We are Accountable – We say what we will do, and then do what we say.
# We Perform – We use our skills, relationships, and reputation to deliver value to our customers, suppliers, and owners.

Initially we are building our business from low-tech through printing promotional offers and retailer messages on ATM and EFTPOS receipts, but as soon as cash flow supports it we will be engaging in high-tech real-time targeted offers to the specific consumer through video wall offers as people are at the checkout or walking through the shopping centre.

I'd like the PowerPoint template to reflect our vision and values.

The PowerPoint template will be used in communicating our proposals to our clients, and needs to catch and hold our audiences attention.

Please check out the web site we have just launched - it is pretty basic but it has only been up a week. We intend to sharpen it over the coming weeks, but you'll get the idea of what our core messages are.

I have recently sourced a logo from ArtHarbor, plus business cards, and have attached the source files for your reference.
Updates

Hi everybody.  Thanks for the designs submitted so far.  Your submissions have helped me understand what I do and don't prefer, and I have updated the "Must Have/Nice to Have/Shouldn't Have" criteria accordingly.  I have also uploaded a powerpoint template that I had at a company I udsed to run that has the sort of visual theme I find appealing. I have more time to provide feedback now that the week is over, so I will comment on individual designs shortly, and I will respond to queries directed to me.

Kind Regards - Grant

Target Market(s)

Our customers are large corporations that have professional Point Of Sale marketing experts looking for a supplier with an edge over others in a crowded market. The buyer of our product and services is ultimately a communications expert. They want to see distinctive competence, and an agility of thinking that will make them money through driving more consumer spending.

Industry/Entity Type

Financial

Font styles to use
Sans Serif

Colors
34a7d7
0892cd
3276b5

Requirements
Must have
• The following Slides: Title Slide, Agenda, About Kelvanta, Thank you
The pages must be easy on the eye.
The final product must be a PowerPoint template file with the usual "Title", "Title and Content", "Title & Table", and "Blank" page types.
Widescreen format please.
Nice to have
• The pages should have an eye-catching visual element running through all the pages. I have attached a template from a company i used to be involved with that has a visual theme running through it that I like.
Plenty of whitespace - have a look at www.kelvanta.net.
Bonus points for pulling the text from the brief into the template.
Use "Innovation - Integrity - Service" as the tag line.
Should not have
• Pages should not be busy.
Stay away from too much black. I know the cards have black, but the presentation shouldn't.
I dont like serifed fonts. Use Dravelle's Modern UI style for insporation.
The "Bringing Lumora" tag line was an invention of the logo designer that we do not want to cary forward. Please do not use it.

```html
<!DOCTYPE html>
<html lang="en">
<head>
<meta charset="utf-8">
<title>Kelvanta – Who we are</title>
<link rel="stylesheet" href="https://fonts.googleapis.com/css2?family=Open+Sans:wght@300;400;600;700&display=swap">
<style>
  :root {
    --sky: #34a7d7;
    --brand: #0892cd;
    --deep: #3276b5;
    --ink: #1a1a1a;
    --grey: #8a8a8a;
    --rule: #eeeeee;
    --white: #ffffff;
    --night-1: #040b10;
    --night-2: #12384f;
    --night-3: #2a5a77;
  }
  * { margin: 0; padding: 0; box-sizing: border-box; }
  html, body { width: 1200px; height: 1000px; overflow: hidden; background: var(--white); }
  body { position: relative; font-family: "Open Sans", sans-serif; }

  .brand-header { position: absolute; left: 183px; top: 222px; width: 830px; text-align: center; }
  .brand-lockup { display: inline-flex; align-items: center; gap: 12px; height: 50px; }
  .brand-name { font-weight: 700; font-size: 38px; color: var(--brand); letter-spacing: -0.5px; line-height: 1; }
  .brand-dot { width: 36px; height: 36px; border: 2px solid var(--brand); border-radius: 50%; }
  .header-rule { position: absolute; left: 183px; top: 273px; width: 830px; height: 1px; background: var(--rule); }
  .tagline { position: absolute; left: 183px; top: 278px; width: 830px; text-align: center;
    font-size: 11px; letter-spacing: 1.2px; color: var(--ink); }
  .tagline .accent { color: var(--brand); }
  .tagline .sep { margin: 0 6px; }

  .welcome-band { position: absolute; left: 183px; top: 463px; width: 830px; height: 38px; background: var(--sky);
    color: var(--white); font-weight: 300; font-size: 16px; letter-spacing: 0.3px;
    display: flex; align-items: center; justify-content: flex-end; padding-right: 78px; }

  .hero-banner { position: absolute; left: 183px; top: 501px; width: 830px; height: 80px;
    background:
      radial-gradient(ellipse 180px 60px at 440px 30px, rgba(150,170,180,0.45), transparent 70%),
      radial-gradient(ellipse 260px 80px at 300px 50px, rgba(42,90,119,0.8), transparent 75%),
      linear-gradient(90deg, var(--night-1) 0%, var(--night-2) 25%, var(--night-3) 55%, var(--night-2) 80%, var(--night-1) 100%); }
  .hero-brand { position: absolute; left: 79px; top: 22px; display: flex; align-items: center; gap: 10px; }
  .hero-brand .brand-name { font-size: 26px; }
  .hero-brand .brand-dot { width: 28px; height: 28px; }
  .hero-tagline { position: absolute; right: 78px; top: 24px; color: var(--white); font-size: 11px; }
  .hero-tagline svg { display: block; }

  .intro { position: absolute; left: 340px; top: 628px; width: 511px; text-align: right; }
  .intro-title { font-weight: 300; font-size: 38px; color: var(--deep); letter-spacing: -0.5px; line-height: 52px; }
  .intro-text { margin-top: 20px; font-weight: 300; font-size: 23px; line-height: 30px; color: var(--grey); letter-spacing: -0.2px; }
  .intro-text .brand-word { color: var(--brand); }

  .nav-band { position: absolute; left: 183px; top: 915px; width: 830px; height: 38px; background: var(--sky);
    display: flex; align-items: center; justify-content: space-between; padding: 0 79px; }
  .nav-link { display: flex; align-items: center; gap: 7px; color: var(--white); font-weight: 300; font-size: 16px; letter-spacing: -0.3px; }
</style>
</head>
<body>
  <header class="brand-header">
    <div class="brand-lockup">
      <span class="brand-name">Kelvanta</span>
      <span class="brand-dot"></span>
    </div>
  </header>
  <div class="header-rule"></div>
  <p class="tagline">Innovation<span class="sep">|</span><span class="accent">Integrity</span><span class="sep">|</span>Service</p>

  <div class="welcome-band">Welcome to this Presentation</div>

  <section class="hero-banner" role="img" aria-label="Dark blue textured abstract backdrop">
    <div class="hero-brand">
      <span class="brand-name">Kelvanta</span>
      <span class="brand-dot"></span>
    </div>
    <div class="hero-tagline">
      <svg width="170" height="36" viewBox="0 0 170 36" aria-label="Innovation, Integrity, Service">
        <text x="0" y="23" fill="#ffffff" font-family="Open Sans, sans-serif" font-size="11">Innovation</text>
        <text x="69" y="23" fill="#ffffff" font-family="Open Sans, sans-serif" font-size="11">Integrity</text>
        <text x="126" y="23" fill="#ffffff" font-family="Open Sans, sans-serif" font-size="11">Service</text>
        <path d="M48 31 Q58 37 68 30" fill="none" stroke="#ffffff" stroke-width="1.5"/>
        <path d="M64 28 L69 29 L67 34" fill="none" stroke="#ffffff" stroke-width="1.5"/>
        <path d="M108 13 Q117 3 127 10" fill="none" stroke="#ffffff" stroke-width="1.5"/>
        <path d="M122 6 L128 10 L123 13" fill="none" stroke="#ffffff" stroke-width="1.5"/>
      </svg>
    </div>
  </section>

  <section class="intro">
    <h1 class="intro-title">Who we are...</h1>
    <p class="intro-text"><span class="brand-word">Kelvanta</span> is an exciting new start-up targeting innovative ways to engage with retail customers at the point of sale.</p>
  </section>

  <nav class="nav-band">
    <span class="nav-link">
      <svg width="14" height="14" viewBox="0 0 14 14"><circle cx="7" cy="7" r="6" fill="none" stroke="#1d3b55" stroke-width="1.3"/><path d="M8.5 4 L5 7 L8.5 10 Z" fill="#1d3b55"/></svg>
      Home
    </span>
    <span class="nav-link">
      What We Do
      <svg width="14" height="14" viewBox="0 0 14 14"><circle cx="7" cy="7" r="6" fill="none" stroke="#1d3b55" stroke-width="1.3"/><path d="M5.5 4 L9 7 L5.5 10 Z" fill="#1d3b55"/></svg>
    </span>
  </nav>
</body>
</html>
```